Professional IT Company Letterhead

We need a new letterhead design to incorporate our new login and business card design recently received here on Pixel Meadow. We want the same look and feel as the other two accepted projects. We want a professional and clean design.

Target Market(s)

Medical/Dental and Professional Services Businesses (CPA, Attorney, Architect etc)

Industry/Entity Type

Business

Requirements
Must have
• Clean and professional, consistent brand with our current design of our new logo and business cards.
Nice to have
• Would like to also be able to use the design on our newsletter header

```html
<!DOCTYPE html>
<html lang="en">
<head>
<meta charset="utf-8">
<title>Tidewell Letterhead Set</title>
<link rel="stylesheet" href="https://fonts.googleapis.com/css2?family=Open+Sans:wght@400;600&display=swap">
<style>
  :root {
    --backdrop: #74cfef;
    --paper: #ffffff;
    --brand-blue: #2b8fd6;
    --brand-faint: #b9def4;
    --contact-blue: #3aa0dc;
    --ink: #3a3a3a;
    --shadow: rgba(20, 60, 90, 0.35);
  }
  * { margin: 0; padding: 0; box-sizing: border-box; }
  html, body { width: 1200px; height: 717px; overflow: hidden; }
  body {
    background: var(--backdrop);
    font-family: "Open Sans", Arial, sans-serif;
    position: relative;
  }
  .sheet {
    position: absolute;
    top: 90px;
    width: 367px;
    height: 520px;
    background: var(--paper);
    box-shadow: 8px 10px 14px var(--shadow);
    overflow: hidden;
  }
  .sheet--one { left: 24px; }
  .sheet--two { left: 410px; }
  .sheet--three { left: 803px; }

  .brand-name {
    position: absolute;
    font-weight: 600;
    color: var(--brand-blue);
    font-size: 23px;
    letter-spacing: -0.5px;
    line-height: 1;
  }
  .brand-watermark {
    position: absolute;
    font-weight: 400;
    color: var(--brand-faint);
    line-height: 1;
    letter-spacing: -1px;
    white-space: nowrap;
  }
  .brand-watermark--footer { left: 14px; top: 442px; font-size: 51px; }
  .brand-watermark--feature { left: 62px; top: 419px; font-size: 65px; }

  .contact {
    position: absolute;
    font-size: 5px;
    line-height: 9px;
    color: var(--contact-blue);
    white-space: nowrap;
  }
  .address { color: var(--ink); }
  .contact--right { text-align: right; }
</style>
</head>
<body>

  <section class="sheet sheet--one">
    <div class="brand-name" style="top:40px; right:45px;">Tidewell</div>
    <div class="brand-watermark brand-watermark--footer">Tidewell</div>
    <div class="contact contact--right" style="right:8px; top:472px;">
      <div>+1 555 014 2200</div>
      <div>hello@tidewell.net</div>
    </div>
    <div class="contact" style="left:218px; top:481px;">www.tidewell.net</div>
    <div class="contact address" style="left:216px; top:491px;">physical address and location related information here</div>
  </section>

  <section class="sheet sheet--two">
    <div class="brand-name" style="top:40px; left:45px;">Tidewell</div>
    <div class="contact" style="right:18px; top:56px;">www.tidewell.net</div>
    <div class="brand-watermark brand-watermark--footer">Tidewell</div>
    <div class="contact contact--right" style="right:23px; top:472px;">
      <div>+1 555 014 2200</div>
      <div>hello@tidewell.net</div>
      <div class="address">physical address and location related information here</div>
    </div>
  </section>

  <section class="sheet sheet--three">
    <div class="contact" style="left:33px; top:40px;">
      <div>+1 555 014 2200</div>
      <div>hello@tidewell.net</div>
      <div class="address" style="margin-top:2px;">physical address and location related information here</div>
      <div style="margin-top:2px;">www.tidewell.net</div>
    </div>
    <div class="brand-name" style="top:40px; right:48px;">Tidewell</div>
    <div class="brand-watermark brand-watermark--feature">Tidewell</div>
  </section>

</body>
</html>
```